Boat Detail Postcard Design

We are looking for a postcard design for a boat detailing company called "Tidewell Gleam Detailing" in Madeira Beach, Florida. It is a veteran owned small business. We make sure to give customers a show room finish that is inspection ready the, first time, every time. Our services include: deep clean, compound & wax, bottom scrapping,and satisfaction guaranteed. We would like to incorporate garnet as the color for the company name and water droplets or water and we would like to maintain a professional appearance.

Target Market(s)

ages 25-75 that own boats and are of upper or upper middle class

Industry/Entity Type

Business

```html
<!DOCTYPE html>
<html lang="en">
<head>
<meta charset="utf-8">
<title>Tidewell Gleam Detailing – Postcard</title>
<link rel="stylesheet" href="https://fonts.googleapis.com/css2?family=Source+Sans+3:ital,wght@0,400;0,600;1,400&display=swap">
<style>
  :root {
    --garnet: #8e1f1f;
    --sky-top: #d8eef8;
    --sky-bottom: #f4fafd;
    --ink: #4a4f55;
    --sea-light: #6fbcc8;
    --sea-mid: #1f7f98;
    --sea-deep: #0d4f73;
    --boat-grey: #cfd2d6;
    --boat-magenta: #9a3a7c;
    --white: #ffffff;
  }
  * { margin: 0; padding: 0; box-sizing: border-box; }
  html, body { width: 1200px; height: 930px; overflow: hidden; }
  body { font-family: "Source Sans 3", sans-serif; background: var(--sky-bottom); }

  .postcard {
    position: relative;
    width: 1200px;
    height: 930px;
    overflow: hidden;
    background: linear-gradient(180deg, var(--sky-top) 0%, var(--sky-bottom) 55%);
  }

  .scene { position: absolute; left: 0; top: 0; width: 1200px; height: 930px; }

  .company-name {
    position: absolute;
    left: 100px;
    top: 76px;
    font-size: 66px;
    font-weight: 600;
    line-height: 1;
    color: var(--garnet);
  }

  .intro {
    position: absolute;
    left: 102px;
    top: 214px;
    font-size: 23px;
    line-height: 32px;
    color: var(--ink);
    white-space: nowrap;
  }

  .services {
    position: absolute;
    left: 411px;
    top: 214px;
    list-style: none;
    font-size: 23px;
    line-height: 32px;
    font-style: italic;
    color: var(--ink);
  }
  .services li::before { content: "• "; }

  .tagline {
    position: absolute;
    left: 0;
    top: 762px;
    width: 1200px;
    font-size: 31px;
    line-height: 40px;
    font-style: italic;
    color: var(--white);
  }
  .tagline .line-one { display: block; padding-left: 168px; }
  .tagline .line-two { display: block; padding-left: 316px; }
</style>
</head>
<body>
  <main class="postcard">
    <svg class="scene" viewBox="0 0 1200 930" xmlns="http://www.w3.org/2000/svg">
      <defs>
        <linearGradient id="sea" x1="0" y1="0" x2="0" y2="1">
          <stop offset="0" stop-color="#6fbcc8"/>
          <stop offset="0.3" stop-color="#1f7f98"/>
          <stop offset="1" stop-color="#0d4f73"/>
        </linearGradient>
        <linearGradient id="boat-area" x1="0" y1="0" x2="1" y2="0">
          <stop offset="0" stop-color="#cfd2d6"/>
          <stop offset="1" stop-color="#9a3a7c"/>
        </linearGradient>
      </defs>
      <path role="img" aria-label="Illustration area: ocean waves with white spray"
            d="M0 520 C200 490 420 500 600 510 C800 495 1000 480 1200 485 L1200 930 L0 930 Z"
            fill="url(#sea)"/>
      <rect role="img" aria-label="Illustration area: speedboat with grey deck and magenta hull cutting through the water"
            x="410" y="365" width="790" height="335" rx="24"
            fill="url(#boat-area)" opacity="0.55"/>
    </svg>

    <h1 class="company-name">Tidewell Gleam Detailing</h1>

    <p class="intro">A veteran owned small<br>business specializing in<br>boat detailing located in<br>Madeira Beach, Florida.</p>

    <ul class="services">
      <li>Deep Clean</li>
      <li>Compound &amp; Wax</li>
      <li>Bottom Scrapping</li>
      <li>Satisfaction Guaranteed</li>
    </ul>

    <p class="tagline">
      <span class="line-one">“We make sure to give customers a show room finish</span>
      <span class="line-two">that is inspection ready the, first time, every time!”</span>
    </p>
  </main>
</body>
</html>
```